Website Redesign for Technology Focused Investment Bank

We need a website redesign for a technology and digital media focused investment banking firm. Think modern and forward thinking yet stable and smart. We provide mergers and acquisitions advisory services to our clients. Our target market are CEO's and CFO's (senior executives) that run and operate technology firms.

Larkstone Capital Partners - www.larkstonecapitalpartners.example

We are headquartered in Los Angeles, CA. Please do NOT use the Pemberly marker for anything.

We have the content and can update the photos as well.

We are looking for a "template" website we can update and edit with ease.

A competitive firm's website is: www.brackenhale.example Not sure I like it but I want it to look way better then this one.

Looking for a more modern version. Not too stuffy and conservative, please. Elegant, smart, updated and progressive/modern.
Updates

Color preferences:  Blue's including matching logo color. Grey's. You can add other colors if it flows well and looks clean and nice.

Menu:  Drop Down

Open to platform...please use one that most people can use, is reasonably priced if I need to buy it, and easy to update monthly and sometimes weekly.

Please use this website as a good example of what we are looking for (or similar version of it): www.quelmora.example

Thanks!
Derek P.

We are reviewing all submissions and will select one this week. Thank you everyone for your outstanding and creative designs you have sent us. We really appreciate it.

Thanks for everyone's hard work and creative input into our website design. We really appreciate it!

Target Market(s)

CEO's and CFO's, Entrepreneurs and Board Members of Technology Companies.

Industry/Entity Type

Investment

Font styles to use
Sans Serif

Colors
33a6d7
0492cd
0555a3
3176b5
85abd2
333333
5c5c5c
757575

Requirements
Must have
• Links to social media including Quillnet, LinkedIn, Google+, Facebook, etc.

Must try to match logo color
Should not have
• No conservative, old looking colors or background. For example, no green marble look.

```html
<!DOCTYPE html>
<html lang="en">
<head>
<meta charset="utf-8">
<title>Larkstone Capital Partners</title>
<link rel="stylesheet" href="https://fonts.googleapis.com/css2?family=Arimo:wght@400;700&family=Roboto+Condensed:wght@700&display=swap">
<style>
:root{
  --blue-dark:#0d3f7e;
  --blue:#0555a3;
  --blue-mid:#3176b5;
  --blue-light:#85abd2;
  --ink:#333333;
  --ink-mid:#5c5c5c;
  --ink-soft:#757575;
  --grey-band:#e8e8e8;
  --footer:#2a2a2a;
  --footer-text:#7a7a7a;
  --white:#ffffff;
}
*{margin:0;padding:0;box-sizing:border-box}
html,body{width:972px;height:1200px;overflow:hidden;background:var(--white)}
body{position:relative;font-family:"Arimo",Arial,sans-serif;color:var(--ink)}
a{color:inherit;text-decoration:none}
.abs{position:absolute}

/* header */
.brand{left:140px;top:7px;display:flex;align-items:center;gap:13px}
.brand-mark{width:52px;height:52px;border-radius:50%;background:var(--blue-mid)}
.brand-name{font-size:15.5px;color:var(--blue);font-weight:400}
.lang{left:763px;top:15px;width:69px;height:19px;border:1px solid #bbb;border-radius:3px;font-size:8px;color:var(--ink);display:flex;align-items:center;gap:5px;padding-left:6px;background:#f7f7f7}
.lang-swatch{width:13px;height:9px;background:var(--blue-dark)}
.top-nav{left:519px;top:41px;display:flex;font-size:9.5px;color:var(--ink)}
.top-nav a{width:0;white-space:nowrap}
.main-nav{left:0;top:69px;width:972px;height:31px;background:linear-gradient(#2a67ab,#0d4a92)}
.main-nav a{position:absolute;top:10px;font-size:9.5px;color:var(--white)}

/* hero */
.hero{left:0;top:100px;width:972px;height:406px;background:linear-gradient(135deg,#1e1e1e,#111 60%,#1a1a1a)}
.hero-person{left:640px;top:105px;width:128px;height:400px;background:linear-gradient(#3a3a40,#1d1d22);border-radius:40px 40px 4px 4px}
.hero-title{right:408px;top:184px;text-align:right;font-family:"Roboto Condensed","Arial Narrow",sans-serif;font-weight:700;color:var(--white);font-size:34px;line-height:42px}
.hero-sub{right:408px;top:279px;font-size:14.5px;color:var(--white);white-space:nowrap}
.hero-copy{right:408px;top:308px;text-align:right;font-size:11.5px;line-height:23px;color:#e6e6e6;white-space:nowrap}
.hero-btn{left:351px;top:376px;width:212px;height:41px;border-radius:21px;background:linear-gradient(#8a8a8a,#4a4a4a);color:var(--white);font-size:13.5px;display:flex;align-items:center;justify-content:center;box-shadow:0 2px 4px rgba(0,0,0,.5)}
.dots{left:455px;top:478px;display:flex;gap:3px}
.dots span{width:8px;height:8px;border-radius:50%;background:#888}
.dots span.on{background:var(--blue-mid)}

/* welcome */
.welcome-mark{left:148px;top:553px;width:47px;height:47px;border-radius:50%;background:var(--blue-mid)}
.welcome-hello{right:619px;top:545px;font-size:13px;color:var(--blue)}
.welcome-name{right:619px;top:568px;font-size:13px;color:var(--blue)}
.welcome-brace{left:372px;top:536px}
.welcome-copy{left:400px;top:543px;width:440px;font-size:8px;line-height:15.3px;color:var(--ink)}
.rule{left:139px;top:620px;width:694px;height:1px;background:#c8c8c8}

/* sectors */
.sector{top:647px;width:216px}
.sector h3{font-size:11.5px;font-weight:400;color:var(--blue);margin-bottom:10px}
.sector-img{width:216px;height:106px}
.sector p{margin-top:12px;width:212px;font-size:8.6px;line-height:16.6px;color:var(--ink)}
.sector .btn{margin-top:9px;display:inline-flex;width:71px;height:22px;align-items:center;justify-content:center;background:var(--blue);border-radius:2px;color:var(--white);font-size:8px}

/* subscribe */
.subscribe{left:139px;top:907px;width:694px;height:66px;background:var(--grey-band);border-left:6px solid var(--blue)}
.subscribe h4{position:absolute;left:12px;top:16px;font-size:11.5px;font-weight:400;color:var(--blue)}
.subscribe p{position:absolute;left:12px;top:39px;font-size:9.5px;color:var(--ink)}
.email{position:absolute;left:422px;top:21px;width:166px;height:25px;background:var(--white);border:1px solid #bbb;border-radius:2px;font-size:9px;color:#999;padding:7px 10px}
.sub-btn{position:absolute;left:601px;top:21px;width:76px;height:25px;background:linear-gradient(#5c6470,#3a4049);border-radius:2px;color:var(--white);font-size:9.5px;display:flex;align-items:center;justify-content:center}

/* footer */
.footer{left:0;top:998px;width:972px;height:202px;background:var(--footer)}
.fcol{top:1030px;width:176px}
.fcol h5{font-size:11.5px;font-weight:400;color:#b5b5b5;margin-bottom:9px}
.fcol p{font-size:7px;line-height:14.5px;color:var(--footer-text)}
.fcol .lite{color:#d8d8d8;font-size:7.5px}
.tweet{margin-bottom:8px}
.tweet .link{color:#d8d8d8;font-size:7.5px;line-height:12px}
.tweet .when{font-style:italic;font-size:6.5px;color:#aaa}
.social{display:flex;gap:5px;margin-top:10px}
.social span{width:23px;height:23px;border-radius:50%;background:#4a4a4a;border:1px solid #555}
.bottom-links{left:140px;top:1178px;font-size:7.5px;color:var(--footer-text)}
.bottom-links span{margin:0 10px}
.copyright{right:143px;top:1178px;font-size:7.5px;color:var(--footer-text)}
</style>
</head>
<body>

<header>
  <div class="abs brand"><div class="brand-mark"></div><span class="brand-name">Larkstone Capital Partners</span></div>
  <div class="abs lang"><span class="lang-swatch"></span>English ▾</div>
  <nav class="abs top-nav">
    <a>Home</a>
    <a style="margin-left:76px">About Us</a>
    <a style="margin-left:90px">News+Blog</a>
    <a style="margin-left:99px">Contact Us</a>
  </nav>
  <nav class="abs main-nav">
    <a style="left:165px">Services</a>
    <a style="left:245px">Transactions</a>
    <a style="left:342px">Research</a>
    <a style="left:425px">Private Equity</a>
    <a style="left:526px">Recommendations</a>
    <a style="left:646px">About the Founder</a>
    <a style="left:766px">Careers</a>
  </nav>
</header>

<section>
  <div class="abs hero" role="img" aria-label="Dark world map backdrop"></div>
  <div class="abs hero-person" role="img" aria-label="Portrait of a banker in a dark suit"></div>
  <h1 class="abs hero-title">INVESTMENT BANKING<br>M&amp;A ADVISORY</h1>
  <p class="abs hero-sub">We are technology focussed investment company</p>
  <p class="abs hero-copy">We are an independent investment bank and M&amp;A advisory firm<br>focusedexclusively on the global Technology and Digital Media sectors. Specifically</p>
  <a class="abs hero-btn">Clickhere for more info</a>
  <div class="abs dots"><span class="on"></span><span></span><span></span></div>
</section>

<section>
  <div class="abs welcome-mark"></div>
  <p class="abs welcome-hello">Welcome to</p>
  <p class="abs welcome-name">Larkstone Capital Partners</p>
  <svg class="abs welcome-brace" width="14" height="60" viewBox="0 0 14 60"><path d="M12 2 Q5 2 5 10 L5 24 Q5 30 1 30 Q5 30 5 36 L5 50 Q5 58 12 58" fill="none" stroke="#aaa" stroke-width="2"/></svg>
  <p class="abs welcome-copy">We are an independent investment bank and M&amp;A advisory firm focused exclusively on the global Technology and Digital Media sectors. Specifically, we execute mergers and acquisitions for the Software, IT Services, Internet and Digital Media industry sectors...</p>
  <div class="abs rule"></div>

  <article class="abs sector" style="left:139px">
    <h3>Software</h3>
    <div class="sector-img" role="img" aria-label="Grey jigsaw puzzle pieces" style="background:linear-gradient(135deg,#d8d8d8,#8e8e8e)"></div>
    <p>Our professionals are able to assist with complex strategic and financial M&amp;A transactions within the soft-ware industry.</p>
    <a class="btn">Read More</a>
  </article>
  <article class="abs sector" style="left:378px">
    <h3>IT Services</h3>
    <div class="sector-img" role="img" aria-label="Glass office tower against a blue sky" style="background:linear-gradient(135deg,#c9ccd2,#3b4fa0 60%,#cfd6e2)"></div>
    <p>We provide investment banking and M&amp;A advisory services to some of the largest IT Services firms across the globe.</p>
    <a class="btn">Read More</a>
  </article>
  <article class="abs sector" style="left:617px">
    <h3>Internet and Digital Media</h3>
    <div class="sector-img" role="img" aria-label="Hands exchanging a network cable in a server room" style="background:linear-gradient(90deg,#2a5fa8,#e8eef6 50%,#3d6fb6)"></div>
    <p>We provide investment banking and M&amp;A advisory services to some of the largest IT Services firms across the globe.</p>
    <a class="btn">Read More</a>
  </article>

  <div class="abs subscribe">
    <h4>SUBSCRIBE TO OUR M&amp;A UPDATES</h4>
    <p>Our professionals are able to assist with complex strategic and financial M&amp;A transactions</p>
    <div class="email">Email Id :</div>
    <a class="sub-btn">Subscribe</a>
  </div>
</section>

<footer>
  <div class="abs footer"></div>
  <div class="abs fcol" style="left:141px">
    <h5>Why us ?</h5>
    <p>We are an independent investment bank and M&amp;A advisory firm focused exclusively on the global Technology &nbsp;and Digital Media sectors. Specifically, we execute mergers and acquisitions for the Software, IT Services, &nbsp;Internet and Digital Media industry sectors. - <span class="lite">See more</span></p>
  </div>
  <div class="abs fcol" style="left:380px;width:200px">
    <h5>Quillnet Feeds</h5>
    <div class="tweet"><p style="color:#555">Check out th best Themes online in the world at</p><div class="link">http://lnk.example/k7Qm2</div><div class="when">1 day ago</div></div>
    <div class="tweet"><p style="color:#555">Check out th best Themes online in the world at</p><div class="link">http://lnk.example/k7Qm2</div><div class="when">1 day ago</div></div>
  </div>
  <div class="abs fcol" style="left:620px">
    <h5>Follow Us</h5>
    <p>We are an independent investment bank and M&amp;A advisory firm focused exclusively on the global Technology &nbsp;and Digital Media sectors...</p>
    <div class="social" aria-label="Social links"><span></span><span></span><span></span><span></span></div>
  </div>
  <div class="abs bottom-links">Home<span>|</span>About Us<span>|</span>News+Blog<span>|</span>Contact Us</div>
  <div class="abs copyright">© 2014, Larkstone Capital Partners. All rights reserved.</div>
</footer>

</body>
</html>
```